Web 2.0 my 1 page website ($500 Guaranteed)

Im looking for someone who can update my existing design at http://www.doriselvanby.com
I like existing layout and the way the boxes all work. Looking for the same design but with an updated web 2.0 textured look and feel.
Please note the current site is already working on top of pagecrate and new design needs to also work with pagecrate so I can continue to page content.
Looking for designer who can also get it working in pagecrate as it is today.
$500 AUD first prize for it all working.
If it helps:
I like minimailist. I like white. I like bright. I like texture. I like backgrounds. I like horizontal stripes running the length of the page. I like designs that work regardless of width of page. I like big bold statements. I like obvious. I like round edges. I like sites that look like they have come alive. I like depth. I like a 3D look. I like something very subtle that moves occassionally - just enough to catch your eye. I dont like popups. I dont like scrolling.
I like really clean SEO friendly source code. I like standards compatible design.
http://www.lotvessel.ie/ I like the depth of the mini coming out of the screen. I like the big bold fonts and the bright colours. I like the horizontal red stripe running the length of the page.
http://www.quillharbor.ie/ I like the backround clouds. I like the nice big lettering on the font on the mene bar. I like the nice bog boxes and contact numbers.
http://www.kuljepolkuja.fi/ I like the bright colours on the phone. I like the splash of the bubbles at the top of the page.
http://ontheruncue.me/ I like the blurred background. I REALLY like the rounded enter your email and notify me text boxes. I like the fonts on notify me and the textured background of the button.
http://9qtorn.com/it/ I really like the horizontal bar across the page - I like the big fonts in this background - I like the green and the orange. I really like the depth - how the beans and chair and butterfly sit on top of the page kind of bringing it to life. Like all the layers giving that illusion of 3D.
http://www.fenwrigley.net/ Like the big fonts, the horizontal bar, the leather stitching look around the "lets work together" and how everything is shadowed and sits off the page. I like the big contact us / get in touch / fonts at the bottom the big social media buttons. Probably this area could all be half the size but I like it.
http://www.drevoxis.com/ I like the graining textures in the background grays. I prefer blues and whites.
http://tibbinshedding.ca/ Like the big bold texts and the colours. Like the 3D cardboard box coming off the page.
http://pondchimers.com/ Like the textured backround - the rough grainy blue.
http://www.uk-rv.com/ I always liked those background kind of bursts behind the bay area picture in the middle. Like the striped blue background.
http://workshop.vendoqua.com/ Who doesnt like a ninja, but again like the big fonts and the way the person has depth
http://www.plumfolders.com/ I like the depth. I like the big bold colours.
http://www.5ibrelt.com/ Again like how the product is featured with lighting behind it, has that 3D look. Nice big lettering etc.
Updates
I like minimailist. I like white. I like bright. I like texture. I like
backgrounds. I like horizontal stripes running the length of the page. I
like designs that work regardless of width of page. I like big bold
statements. I like obvious. I like round edges. I like sites that look
like they have come alive. I like depth. I like a 3D look. I like
something very subtle that moves occassionally - just enough to catch
your eye. I dont like popups. I dont like scrolling.
http://www.lotvessel.ie/
I like the depth of the mini coming out of the screen. I like the big
bold fonts and the bright colours. I like the horizontal red stripe
running the length of the page.
http://www.quillharbor.ie/
I like the backround clouds. I like the nice big lettering on the font
on the mene bar. I like the nice bog boxes and contact numbers.
http://ontheruncue.me/
I like the blurred background. I REALLY like the rounded enter your
email and notify me text boxes. I like the fonts on notify me and the
textured background of the button.
http://9qtorn.com/it/
I really like the horizontal bar across the page - I like the big fonts
in this background - I like the green and the orange. I really like the
depth - how the beans and chair and butterfly sit on top of the page
kind of bringing it to life. Like all the layers giving that illusion of
3D.
http://www.fenwrigley.net/
Like the big fonts, the horizontal bar, the leather stitching look
around the "lets work together" and how everything is shadowed and sits
off the page. I like the big contact us / get in touch / fonts at the
bottom the big social media buttons. Probably this area could all be
half the size but I like it.
Typical Components of Web 2.0 Site Design
- Lots of space: Web 2.0 sites tend to have a lot of wide-open space. It's a contrast from the 90s, where the trend was to make usage of every square inch of a website's home page with links, banners and applets. White space is embraced to a major degree, as it calls attention to important buttons and links.
- The "Less Is More" Mentality: By putting less on the page, you're drawing more attention to the elements that matter: content and call-to-action buttons. "Clutter" and Web 2.0 simply do not mix - this is a new era of design psychology.
- Gradients: Merely a design element, gradients are used in Web 2.0 site design to give a clean, soft impression that's easy on the eyes.
- Large Fonts: Huge headings are a popular trend in Web 2.0 design - headings are usually taglines that describe or summarize what a website is about in just a handful of words. It's a huge benefit to first-timer usability, especially since new visitors would like to "get to the point" without having to read an intro paragraph.
- Dramatic Color Contrast: Another typical element seen in Web 2.0 design are bright colors (particularly neon colors) that accent site elements including menus, separator bars and footers. Many sites use this same neon color for their hyperlinks and headings, as well. Sometimes, the contrast between bright neon colors and charcoal or light gray text are put in unison for a dramatic effect.
- Eye Candy Logos: In Web 2.0 logo design, it's almost expected to see logos have a shiny plastic luster, or a soft gradient. Most Web 2.0 fonts are similar to basic Arial, Tahoma or Helvetica, and are simple. The colors used within the logo are also typically mimicked on other site design pieces to create a sense of uniformity.
- Huge Buttons: Calls to action (buttons that prompt you to "Get More Information," "Download Now," "See A Demo" or "Buy Now") are typically gigantic in Web 2.0 design. They're also attractive, featuring a color that strays away from the rest of the website's schematic. These buttons are typically isolated by a great deal of space, making them very easy to notice.
- Reflections: Product images, screenshots and icons can be seen as having "reflections" underneath them, as if they were standing on top of a new laminate floor. It's a stereotypical design element of Web 2.0.
- Lots of Icons: Web 2.0 icons are always in vector format, which is the standard format created by software such as Adobe Illustrator and Flash. They're attractive and clean looking, and are used to either draw attention to a website's sub-categories, a product's individual features, or anything else that the web designer wanted to help associate for a viewer.
- Exaggerated Web Form Fields: Huge form fields add to usability and draw attention to sign-ups and registrations. Instead of typing in a search, a username or anything else into a tiny web field, Web 2.0 has evolved them into massive interactive boxes with large text that makes things easy to see. For a good example, look at Glimvo.com's huge fields.

```html
<!DOCTYPE html>
<html lang="en">
<head>
<meta charset="utf-8">
<title>Doris Elvanby · Retail CIO</title>
<link rel="stylesheet" href="https://fonts.googleapis.com/css2?family=Arimo:wght@400;700&family=Open+Sans:wght@400;600&family=Source+Sans+3:wght@400;600&display=swap">
<style>
:root{
  --ink:#1d1d1d;
  --black:#000;
  --white:#fff;
  --hero-top:#5fc3d8;
  --hero-mid:#3a8fc1;
  --hero-edge:#2c5f9e;
  --navy:#0f2c4a;
  --heading:#2a5b9c;
  --paper:#f4f4f4;
  --footer:#1f4c8f;
  --footer-dark:#163d78;
  --bubble:#0e2a52;
  --accent:#e8453c;
}
*{margin:0;padding:0;box-sizing:border-box}
html,body{width:1200px;height:960px;overflow:hidden;background:var(--white)}
body{font-family:"Source Sans 3",Arial,sans-serif;color:var(--ink)}
.page{position:relative;width:1200px;height:960px;overflow:hidden}

.topbar{position:absolute;left:0;top:0;width:1200px;height:52px;background:var(--black)}
.main-nav{position:absolute;right:141px;top:16px;font-family:"Open Sans",Arial,sans-serif;font-size:12px;letter-spacing:2px;color:var(--white);font-weight:600}
.main-nav a{color:var(--white);text-decoration:none}
.main-nav span{margin:0 9px}

.hero{position:absolute;left:0;top:52px;width:1200px;height:396px;
  background:radial-gradient(ellipse 560px 300px at 720px 110px,var(--hero-top) 0%,var(--hero-mid) 55%,var(--hero-edge) 100%);}
.hero::after{content:"";position:absolute;inset:0;background:repeating-linear-gradient(90deg,rgba(255,255,255,.04) 0 1px,transparent 1px 4px)}
.social{position:absolute;top:19px;display:block;width:22px;height:22px;border-radius:4px;background:#2b2b2b;box-shadow:0 1px 2px rgba(0,0,0,.4);z-index:2}
.social.one{left:1004px}
.social.two{left:1036px}
.tagline{position:absolute;right:176px;top:66px;width:560px;text-align:right;color:var(--white);font-size:20.5px;line-height:28.5px;letter-spacing:-.3px;z-index:2;text-shadow:0 1px 2px rgba(0,0,0,.25)}
.portrait{position:absolute;left:127px;top:-24px;width:300px;height:420px;z-index:1}
.name{position:absolute;z-index:2;font-family:Arimo,Arial,sans-serif;font-weight:700;letter-spacing:-4px;line-height:1}
.name.first{left:320px;top:284px;font-size:92px;color:var(--white);text-shadow:0 3px 6px rgba(0,0,0,.35)}
.name.last{left:646px;top:266px;font-size:84px;color:var(--navy);text-shadow:0 3px 6px rgba(0,0,0,.3)}
.role{position:absolute;right:180px;top:252px;z-index:2;font-family:Arimo,Arial,sans-serif;font-weight:700;font-size:31px;color:var(--white)}

.intro{position:absolute;left:0;top:448px;width:1200px;height:354px;background:var(--paper)}
.intro h1{position:absolute;left:147px;top:32px;font-family:Arimo,Arial,sans-serif;font-weight:700;font-size:30px;color:var(--heading);letter-spacing:.5px}
.intro p{position:absolute;left:148px;width:530px;font-size:15.2px;line-height:24.4px;letter-spacing:-.2px;color:#222}
.intro p.lead{top:91px}
.intro p.story{top:179px}
.showcase{position:absolute;left:690px;top:30px;width:400px;height:304px}

.footer{position:absolute;left:0;top:802px;width:1200px;height:158px;background:linear-gradient(180deg,var(--footer),var(--footer-dark))}
.footer-nav{position:absolute;left:147px;top:35px;font-family:Arimo,Arial,sans-serif;font-size:13.5px;color:var(--white)}
.footer-nav a{color:var(--white);text-decoration:none}
.footer-nav span{margin:0 6px}
.copyright{position:absolute;left:147px;top:79px;font-family:Arimo,Arial,sans-serif;font-size:13.5px;line-height:23px;color:var(--white)}
.copyright a{color:var(--accent);text-decoration:none}
.tweet{position:absolute;left:729px;top:30px;width:332px;height:84px;background:var(--bubble);border-radius:5px;padding:12px 20px;font-family:Arimo,Arial,sans-serif;font-size:13.5px;line-height:16px;color:var(--white)}
.tweet::after{content:"";position:absolute;right:68px;bottom:-22px;border-left:50px solid transparent;border-top:22px solid var(--bubble)}
.tweet a{color:var(--accent);text-decoration:none;font-weight:700}
.tweet .link{font-weight:400}
.tweet time{position:absolute;right:20px;bottom:10px;font-size:11px;font-style:italic}
.feed-name{position:absolute;right:139px;top:124px;font-family:Arimo,Arial,sans-serif;font-weight:700;font-size:20px;color:var(--white)}
</style>
</head>
<body>
<div class="page">
  <header class="topbar">
    <nav class="main-nav"><a href="#">HOME</a><span>|</span><a href="#">ABOUT ME</a><span>|</span><a href="#">BLOG</a><span>|</span><a href="#">CONTACT</a></nav>
  </header>

  <section class="hero">
    <svg class="portrait" role="img" aria-label="Portrait photo of Doris Elvanby in a dark shirt" viewBox="0 0 300 420">
      <defs>
        <linearGradient id="portraitFill" x1="0" y1="0" x2="0" y2="1">
          <stop offset="0" stop-color="#1a2430" stop-opacity=".85"/>
          <stop offset=".7" stop-color="#1c3550" stop-opacity=".8"/>
          <stop offset="1" stop-color="#2c5f9e" stop-opacity="0"/>
        </linearGradient>
      </defs>
      <rect x="0" y="0" width="300" height="420" rx="10" fill="url(#portraitFill)"/>
    </svg>
    <a class="social one" href="#" aria-label="Microblog profile"></a>
    <a class="social two" href="#" aria-label="Professional network profile"></a>
    <p class="tagline">Retail CIO with a passion for multi-channel, multi-store technology. Specialise in online communities to help drive the business by consumer engangement.</p>
    <div class="role">RETAIL CIO</div>
    <div class="name last">Elvanby</div>
    <div class="name first">DORIS</div>
  </section>

  <main class="intro">
    <h1>Hi there...</h1>
    <p class="lead">Hello, and welcome to my home page on the web. There isn't really much going on here, more just a front end for my webmail etc. For those that are interested in learning a bit more about me personally or commercially, feel free to click around and have a look.</p>
    <p class="story">My background is basically a sales guy who a long time ago learnt how to use technology to reach the masses. After running BBS's for years to support our computer business, I built my first commercial web site around 1994 and quickly moved into full blown eCommerce sites. Did a stint next in Web Marketing and SEO which lead to a couple of years of hammering affiliate programs and ad-network ads across the web.</p>
    <svg class="showcase" role="img" aria-label="Screenshots of a web design blog shown as tilted browser windows" viewBox="0 0 400 304">
      <defs>
        <linearGradient id="shotBack" x1="0" y1="0" x2="0" y2="1">
          <stop offset="0" stop-color="#3a3a3a"/><stop offset=".15" stop-color="#e6e6e6"/><stop offset="1" stop-color="#cfcfcf"/>
        </linearGradient>
        <linearGradient id="shotFront" x1="0" y1="0" x2="0" y2="1">
          <stop offset="0" stop-color="#2a2a2a"/><stop offset=".1" stop-color="#fafafa"/><stop offset="1" stop-color="#eeeeee"/>
        </linearGradient>
      </defs>
      <polygon points="76,12 386,2 386,266 76,256" fill="url(#shotBack)" opacity=".75"/>
      <polygon points="8,44 318,34 318,304 8,284" fill="url(#shotFront)" stroke="#bbb"/>
    </svg>
  </main>

  <footer class="footer">
    <nav class="footer-nav"><a href="#">Home</a><span>|</span><a href="#">About Me</a><span>|</span><a href="#">Blog</a><span>|</span><a href="#">Contact</a></nav>
    <p class="copyright">Copyright (c) 2011 <a href="http://www.doriselvanby.com">www.doriselvanby.com</a><br>Allrights reserved. Privacy Policy</p>
    <div class="tweet">
      <a href="#">DorisElvanby</a> : Just ordered: Shelfwise E-Commerce Leaders Playbook | Shelfwise - <a class="link" href="#">http://sw.ly/K4TA</a>
      <time>4 days ago</time>
    </div>
    <div class="feed-name">chirpline</div>
  </footer>
</div>
</body>
</html>
```